Flyer-Design für Karin Dossow
Zielgruppe
Ich bin psychologische Beraterin und Heilpraktikerin für Psychotherapie. Ich biete ein Coaching speziell für Mütter (meist Mütter mit neugeborenen Babys) an. Dieses Mütter-Coaching will ich bewerben. Die Flyer werden unter anderen an Ärzte und Hebammen weiter gegeben und dort in den Praxen ausliegen.
Aufgabenstellung
In meinem Logo herrschen die Farben orange und grau vor - es wäre schön, wenn sich diese Farben im Flyer wiederfinden würden - evtl. kombiniert mit mittelblau oder einem hellem grün.
Des weiteren möchte ich später Flyer im Din Lang Format (einseitig) mit anderen Angeboten erstellen. Das sollte mit dem Design dann auch möglich sein.
Der Schrifttyp soll bitte Arial sein, passend zum Logo. Ich habe bei Bildarko Fotos zu dem Thema erstanden, die ich stimmig finde. Diese Bilder sollten im Flyer genutzt werden.
Für diesen Flyer hätte ich gerne das Format: Falzblatt mit Wickelfalz - 279 x 219 mm

```html
<!DOCTYPE html>
<html lang="de">
<head>
<meta charset="utf-8">
<title>Flyer Coaching für Mütter – Karin Dossow</title>
<link rel="stylesheet" href="https://fonts.googleapis.com/css2?family=Arimo:wght@400;700&display=swap">
<style>
:root{
  --orange:#e39a2f;
  --orange-dark:#d88a1e;
  --blue:#4a9bd1;
  --blue-dark:#3d8bc2;
  --grey-light:#eeeeee;
  --grey-mid:#d6d6d6;
  --grey-text:#4a4a4a;
  --grey-dark:#7a7a7a;
  --ink:#2d2d2d;
  --white:#ffffff;
  --stage:#e4e4e4;
}
*{box-sizing:border-box;margin:0;padding:0}
html,body{width:1200px;height:600px;overflow:hidden;background:var(--stage);font-family:"Arimo",Arial,sans-serif;color:var(--grey-text)}
.canvas{position:relative;width:1200px;height:600px}
.brochure{position:absolute;top:60px;width:570px;height:480px;display:flex;box-shadow:0 4px 14px rgba(0,0,0,.18)}
.brochure--inside{left:20px}
.brochure--outside{left:610px}
.panel{position:relative;width:190px;height:100%;overflow:hidden}
.photo{width:100%}
p{font-size:6.4px;line-height:1.38}

/* inside – situation */
.situation{background:var(--orange);display:flex;flex-direction:column}
.situation .photo{height:175px;background:linear-gradient(160deg,#cfd6e0,#8c95a6 60%,#b8bfcb)}
.situation__title{position:absolute;left:14px;top:112px;font-weight:700;font-size:22px;line-height:1;color:var(--ink);background:rgba(255,255,255,.55);padding:4px 6px}
.situation__list{list-style:none;padding:16px 14px 0 14px;color:var(--white)}
.situation__list li{font-size:6.4px;line-height:1.4;margin-bottom:10px;padding-left:7px;position:relative}
.situation__list li::before{content:"•";position:absolute;left:0}

/* inside – support */
.support{background:linear-gradient(90deg,var(--grey-mid),var(--grey-light) 40%,var(--white));padding:28px 14px 0 16px}
.support__title{font-weight:700;font-size:17px;line-height:1.05;color:var(--ink);margin-bottom:14px}
.support__head{font-weight:700;font-size:11px;color:var(--orange);margin:12px 0 4px}
.support p{margin-bottom:6px}
.support__note{position:absolute;left:12px;right:12px;bottom:24px;background:var(--grey-dark);color:var(--white);border-radius:12px;padding:8px 12px;font-size:5.4px;line-height:1.4;text-align:center}

/* inside – path */
.path{background:var(--blue);padding:26px 14px 0 14px;color:var(--white)}
.path__title{font-weight:700;font-size:20px;line-height:1}
.path__sub{font-size:5.8px;text-transform:uppercase;margin:4px 0 16px;line-height:1.3}
.step{display:flex;align-items:center;gap:9px;margin-bottom:15px}
.step p{font-size:6.4px;line-height:1.45}
.icon{flex:0 0 26px;width:26px;height:26px;border-radius:50%;background:var(--orange);display:flex;align-items:center;justify-content:center}
.icon svg{width:15px;height:15px;stroke:var(--white);fill:none;stroke-width:1.6;stroke-linecap:round}

/* outside – why */
.why{background:var(--orange);display:flex;flex-direction:column}
.why__top{padding:20px 14px 12px;color:var(--white)}
.why__top h2{font-size:12.5px;line-height:1.15;font-weight:700}
.why__top p{font-size:5.6px;margin-top:6px;font-weight:700}
.why__band{background:linear-gradient(90deg,var(--grey-light),var(--grey-mid));padding:14px 18px;font-weight:700;font-size:14.5px;line-height:1.1;color:var(--ink)}
.why__body{padding:14px 14px 0 16px;color:var(--white)}
.why__body p{margin-bottom:9px;font-size:6px}
.why__start{width:72px}
.badge{position:absolute;right:10px;bottom:40px;width:92px;height:92px;border-radius:50%;background:var(--grey-light);border:3px solid var(--white);display:flex;align-items:center;justify-content:center;text-align:center;color:var(--orange);font-weight:700;font-size:8.6px;line-height:1.35;padding:10px}

/* outside – services */
.services{background:var(--grey-light);display:flex;flex-direction:column}
.brand{padding:22px 14px 10px 22px}
.brand__name{font-size:15px;font-weight:700;color:var(--grey-dark);display:flex;align-items:center;gap:5px}
.brand__dot{width:8px;height:8px;border-radius:50%;background:var(--orange)}
.brand__claim{font-size:8px;font-weight:700;color:var(--orange);margin-top:10px}
.brand__sub{font-size:4.8px;color:var(--ink)}
.offer{background:var(--blue);color:var(--white);padding:12px 10px 8px 10px}
.offer__item{display:flex;gap:7px;margin-bottom:10px}
.offer__item h3{font-size:8px;font-weight:700;margin-bottom:2px}
.offer__item p{font-size:5.5px;line-height:1.35}
.contact{padding:14px 14px 0 18px;font-size:5.8px;line-height:1.4;color:var(--ink)}
.contact__invite{color:var(--orange);font-weight:700;margin-bottom:6px}
.contact__name{color:var(--orange);font-weight:700}
.contact strong{display:block}
.contact__phone{color:var(--orange);font-weight:700;margin:3px 0 4px}
.contact__block{margin-top:5px}

/* outside – cover */
.cover{background:linear-gradient(90deg,var(--grey-light),var(--white))}
.cover .photo{height:210px;background:linear-gradient(150deg,#e9ddd2,#c9b2a0 55%,#9aa4b4)}
.cover__claim{padding:22px 14px 0 20px;font-size:13.5px;line-height:1.55;color:var(--ink)}
.cover__claim b{font-weight:700}
.cover__brand{position:absolute;left:22px;bottom:72px;font-size:15px;font-weight:700;color:var(--grey-dark);display:flex;align-items:center;gap:5px}
.cover__band{position:absolute;left:0;right:0;bottom:12px;height:38px;background:var(--orange);color:var(--white);padding:7px 0 0 20px}
.cover__band strong{display:block;font-size:8.6px}
.cover__band span{font-size:4.8px}
.cover__strip{position:absolute;left:0;right:0;bottom:0;height:12px;background:var(--blue)}
</style>
</head>
<body>
<main class="canvas">

  <!-- Innenseite -->
  <section class="brochure brochure--inside">
    <article class="panel situation">
      <div class="photo" role="img" aria-label="Foto: erschöpfte junge Mutter mit schlafendem Baby"></div>
      <h2 class="situation__title">IHRE<br>SITUATION</h2>
      <ul class="situation__list">
        <li>Haben Sie sich Ihr Mutterglück anders vorgestellt? - Sie hatten sich so auf Ihr Baby gefreut, aber die Realität ist gar nicht so, wie Sie sich das gedacht haben?</li>
        <li>Oder Sie haben bereits ein oder mehrere Kinder aber trotzdem ist jetzt alles anders?</li>
        <li>Fühlen Sie sich allein, isoliert: Ihre Kollegen und Freunde führen weiterhin Ihr früheres Leben - Sie sind aber nicht mehr mit dabei?</li>
        <li>Das Verständnis Ihrer Umgebung für Ihre neue Situation fehlt. Sogar die Partnerschaft ist plötzlich ganz anders als sie es vorher war?</li>
        <li>Sie werden nur noch als Mutter wahrgenommen - kaum mehr als die Frau und die Persönlichkeit, die Sie vorher waren und auch immer noch sind?</li>
        <li>Sie fühlen sich oft erschöpft, ratlos, überfordert, unverstanden?</li>
      </ul>
    </article>

    <article class="panel support">
      <h2 class="support__title">MEINE<br>UNTERSTÜTZUNG</h2>
      <h3 class="support__head">BEGLEITUNG</h3>
      <p>Die gute Nachricht: Sie müssen diese belastende Situation nicht allein bewältigen - erleben Sie Erleichterung, indem Sie sich von mir beraten lassen.</p>
      <p>Als Coach gehe ich ganz individuell auf Ihre Person und auf Ihre persönliche Situation ein.</p>
      <h3 class="support__head">STÄRKUNG</h3>
      <p>Entscheiden Sie sich für einen Weg, der zu Ihnen passt und Sie glücklich macht.</p>
      <p>Finden Sie die Mutterrolle, die es Ihnen ermöglicht, gut für sich zu sorgen und bei sich zu bleiben. Leben Sie so Ihre Bedürfnisse und Interessen im Einklang mit denen Ihrer Familie.</p>
      <h3 class="support__head">BERATUNG</h3>
      <p>Trotz einer Flut an Informationen fühlen sich viele Mütter mit ihren Themen alleine gelassen, hilflos und überfordert.</p>
      <p>Bei mir bleiben Sie nicht allein und ratlos: zusammen finden wir individuelle Antworten auf Ihre ganz persönlichen Fragen.</p>
      <div class="support__note">Hinweis: Es handelt sich hier um eine Beratung und nicht um eine Psychotherapie oder sonstige Heilkunde im gesetzlichen Sinne und soll diese auch nicht ersetzen.</div>
    </article>

    <article class="panel path">
      <h2 class="path__title">UNSER WEG</h2>
      <p class="path__sub">Gemeinsam können wir uns Ihre Themen ansehen und bearbeiten</p>
      <div class="step"><span class="icon"><svg viewBox="0 0 16 16"><circle cx="8" cy="4" r="2"/><path d="M3 13h10M5 9l3-2 3 2M5 13l3-3 3 3"/></svg></span><p>Stressbewältigung - finden Sie den Weg zu mehr Gelassenheit, zur inneren Ruhe</p></div>
      <div class="step"><span class="icon"><svg viewBox="0 0 16 16"><circle cx="8" cy="8" r="6"/><path d="M8 4v4l3 2"/></svg></span><p>Zeiteinteilung - so passen Sie Ihre Zeit der momentanen Situation an</p></div>
      <div class="step"><span class="icon"><svg viewBox="0 0 16 16"><path d="M8 3v7M8 13v.5"/></svg></span><p>Erhalten Sie mehr Klarheit über Ihre Bedürfnisse und Erwartungen</p></div>
      <div class="step"><span class="icon"><svg viewBox="0 0 16 16"><path d="M4 2v12M8 2v12M12 2v12M2.5 6h3M6.5 10h3M10.5 5h3"/></svg></span><p>Wandeln Sie Unsicherheit in Stabilität um</p></div>
      <div class="step"><span class="icon"><svg viewBox="0 0 16 16"><circle cx="8" cy="7" r="5"/><path d="M6 14h4"/></svg></span><p>Erkennen und nutzen Sie Ihre Stärken und Fähigkeiten</p></div>
      <div class="step"><span class="icon"><svg viewBox="0 0 16 16"><circle cx="5" cy="4" r="1.6"/><circle cx="11" cy="4" r="1.6"/><circle cx="8" cy="8" r="1.3"/><path d="M5 7v7M11 7v7M8 10v4"/></svg></span><p>Familienberatung - so können Sie entgegenkommend miteinander umgehen</p></div>
      <div class="step"><span class="icon"><svg viewBox="0 0 16 16"><circle cx="8" cy="8" r="1.8"/><circle cx="3" cy="4" r="1.2"/><circle cx="13" cy="4" r="1.2"/><circle cx="3" cy="12" r="1.2"/><circle cx="13" cy="12" r="1.2"/><path d="M4 5l3 2M12 5l-3 2M4 11l3-2M12 11l-3-2"/></svg></span><p>Netzwerk - hier finden Sie Verständnis und Unterstützung</p></div>
    </article>
  </section>

  <!-- Außenseite -->
  <section class="brochure brochure--outside">
    <article class="panel why">
      <div class="why__top">
        <h2>WARUM COACHING<br>EXTRA FÜR MÜTTER?</h2>
        <p>Nun! Nur wer gut für sich selbst sorgt, kann auch für andere da sein!</p>
      </div>
      <h2 class="why__band">COACHING<br>FÜR MÜTTER</h2>
      <div class="why__body">
        <p>Als Heilpraktikerin für Psychotherapie und geprüfte psychologische Beraterin habe ich mich besonders auf das Coaching für Mütter spezialisiert.</p>
        <p>Ich setzte dabei die Methode des lösungsorientierten Kurzzeitcoachings ein, das den Fokus auf Stärken und Lösungen legt und nicht die Probleme und Hindernisse in den Vordergrund stellt.</p>
        <p>Das Konzept wird durch Achtsamkeits- und Entspannungsübungen abgerundet. Aspekte der „gewaltfreien“ = wertschätzenden Kommunikation werden für individuelle Konfliktlösungen im familiären Alltag genutzt.</p>
        <p class="why__start">Starten Sie mit einem neuen und liebevollen Blick auf Ihr Leben und auf Ihre Fähigkeiten.</p>
      </div>
      <div class="badge">Sie werden erstaunt sein, was alles in Ihnen wohnt.</div>
    </article>

    <article class="panel services">
      <div class="brand">
        <div class="brand__name"><span class="brand__dot"></span>karindossow</div>
        <div class="brand__claim">COACHING FÜR MÜTTER</div>
        <div class="brand__sub">BEGLEITUNG - STÄRKUNG - BERATUNG</div>
      </div>
      <div class="offer">
        <div class="offer__item"><span class="icon"><svg viewBox="0 0 16 16"><circle cx="8" cy="5" r="2.5"/><path d="M3 14c0-3 2.2-5 5-5s5 2 5 5"/></svg></span><div><h3>EINZELCOACHING</h3><p>Sie können wählen: das Coaching kann in meiner Praxis in Neuss oder gern auch bei Ihnen zu Hause stattfinden, allein oder mit Partner, so wie es gerade für Sie am besten passt.</p></div></div>
        <div class="offer__item"><span class="icon"><svg viewBox="0 0 16 16"><circle cx="8" cy="5" r="2"/><circle cx="3.5" cy="7" r="1.5"/><circle cx="12.5" cy="7" r="1.5"/><path d="M4 14c0-2.5 1.8-4 4-4s4 1.5 4 4"/></svg></span><div><h3>GRUPPENCOACHING</h3><p>Lernen Sie Gleichgesinnte kennen und profitieren Sie in doppelter Hinsicht - nach dem Motto: „Lieber gemeinsam als einsam“.</p></div></div>
        <div class="offer__item"><span class="icon"><svg viewBox="0 0 16 16"><rect x="5" y="2" width="6" height="12" rx="1"/><path d="M7.5 12h1"/></svg></span><div><h3>TELEFONCOACHING</h3><p>Sie bestimmen Ort und Zeit. Dieses Angebot könnte das Richtige für Sie sein, wenn Sie zeitlich oder örtlich gebunden sind.</p></div></div>
      </div>
      <div class="contact">
        <p class="contact__invite">Rufen Sie mich doch einfach unverbindlich an. Ich freue mich auf Sie!</p>
        <div class="contact__name">Karin Dossow</div>
        <strong>Heilpraktikerin für Psychotherapie</strong>
        <strong>Geprüfte Psychologische Beraterin</strong>
        <div class="contact__phone">Telefon: 0170 - 482 15 336</div>
        <div>Email: info@karin-dossow.de</div>
        <div>www.karin-dossow.de</div>
        <div class="contact__block">Praxisgemeinschaft am Park<br>Lindenweg 14<br>41460 Neuss</div>
      </div>
    </article>

    <article class="panel cover">
      <div class="photo" role="img" aria-label="Foto: Mutter hält ihr schlafendes Neugeborenes an der Schulter"></div>
      <h1 class="cover__claim">DAS BABY IST DA<br>UND <b>NICHTS</b><br>IST MEHR<br>WIE ES WAR!</h1>
      <div class="cover__brand"><span class="brand__dot"></span>karindossow</div>
      <div class="cover__band"><strong>COACHING FÜR MÜTTER</strong><span>BEGLEITUNG - STÄRKUNG - BERATUNG</span></div>
      <div class="cover__strip"></div>
    </article>
  </section>

</main>
</body>
</html>
```